Simon & Lorna's Yuletide Unwind Bash

Invitation to a party 60-80 people at a private residence. Age range 30-40s.

Themes: summer/casual/Australian backyard/local community

**For delivery via both email and printed copy**
Would like one document suitable for both purposes or two versions for electronic or paper invitation. I will arrange printing so please prepare it in a suitable format.

Specimen text attached. Address and phone contact to follow by message with successful bidder

Thanks!
Simon

Target Market(s)

Locals, friends. Party attendees will typicaly be parents in their forties who who be leaving the kids at home for a relaxed party night, and walking home afterward

Industry/Entity Type

Community

Font styles to use
Sans Serif

Requirements
Should not have
• Cliche Australiana imagery. No kangaroos etc

```html
<!DOCTYPE html>
<html lang="en">
<head>
<meta charset="utf-8">
<title>Simon &amp; Lorna's Yuletide Unwind Bash – Invitation Set</title>
<link rel="stylesheet" href="https://fonts.googleapis.com/css2?family=Lobster+Two:ital,wght@1,700&family=Montserrat:wght@700&family=Oswald:wght@400&family=Patrick+Hand+SC&display=swap">
<style>
  :root {
    --backdrop: #e9e5df;
    --sky: #bfe3f4;
    --sky-soft: #d7eef6;
    --sand: #fdf6e3;
    --teal: #1596c0;
    --ink: #1d1d1d;
    --sun: #f39a1e;
    --pink: #e0607a;
    --melon: #e9434f;
    --rind: #8cc86a;
    --hat: #cfcfcf;
    --camera: #2f6c9a;
    --orange: #f7a21b;
    --shades: #d8362f;
    --cocktail: #c93d58;
    --bag: #2a8ed0;
    --ring: #e24b3f;
    --star: #f4874b;
  }
  * { box-sizing: border-box; margin: 0; padding: 0; }
  html, body { width: 1200px; height: 900px; overflow: hidden; }
  body { background: var(--backdrop); position: relative; font-family: "Patrick Hand SC", "Comic Sans MS", sans-serif; color: var(--ink); }

  .card { position: absolute; overflow: hidden; box-shadow: 0 6px 16px rgba(0,0,0,.18); }
  .card--main { left: 32px; top: 60px; width: 550px; height: 777px; background: linear-gradient(180deg, var(--sky) 0%, var(--sky-soft) 40%, var(--sand) 75%, #fffdf6 100%); }
  .card--front { left: 631px; top: 60px; width: 530px; height: 370px; background: linear-gradient(180deg, var(--sky) 0%, var(--sky-soft) 100%); }
  .card--details { left: 631px; top: 463px; width: 530px; height: 370px; background: linear-gradient(180deg, var(--sky) 0%, var(--sky-soft) 100%); }

  .art { position: absolute; border-radius: 40%; opacity: .7; }
  .art--flipflops { background: radial-gradient(closest-side, var(--pink), rgba(224,96,122,.25)); }
  .art--hat { background: radial-gradient(closest-side, var(--hat), rgba(207,207,207,.3)); border-radius: 0 0 50% 50%; }
  .art--melon { background: radial-gradient(closest-side, var(--melon) 55%, var(--rind)); border-radius: 0 0 50% 50%; }
  .art--camera { background: radial-gradient(closest-side, var(--camera), rgba(47,108,154,.3)); }
  .art--orange { background: radial-gradient(closest-side, var(--orange), rgba(247,162,27,.35)); border-radius: 50%; }
  .art--shades { background: radial-gradient(closest-side, var(--shades), rgba(216,54,47,.3)); }
  .art--cocktail { background: radial-gradient(closest-side, var(--cocktail), rgba(140,200,106,.35)); }
  .art--bag { background: radial-gradient(closest-side, var(--bag), rgba(243,233,182,.4)); }
  .art--ring { background: radial-gradient(closest-side, var(--ring), rgba(226,75,63,.3)); border-radius: 50%; }
  .art--star { background: radial-gradient(closest-side, var(--star), rgba(244,135,75,.25)); border-radius: 50% 50% 0 0; }
  .art--sun { background: radial-gradient(closest-side, var(--sun), rgba(243,154,30,.1)); border-radius: 50%; }

  .line { position: absolute; text-align: center; left: 0; right: 0; }
  .intro { font-family: "Oswald", "Arial Narrow", sans-serif; font-size: 17px; letter-spacing: 2.4px; line-height: 23px; }
  .hosts { font-family: "Lobster Two", "Brush Script MT", cursive; font-style: italic; font-weight: 700; color: var(--teal); }
  .hosts::before, .hosts::after { content: ""; display: inline-block; width: 26px; height: 3px; background: var(--teal); vertical-align: middle; margin: 0 16px; }
  .rule { position: absolute; height: 3px; background: var(--teal); }
  .title { font-family: "Montserrat", "Arial", sans-serif; font-weight: 700; color: var(--teal); letter-spacing: .5px; }
  .ribbon { position: absolute; }
  .ribbon-text { font-family: "Montserrat", "Arial", sans-serif; font-weight: 700; color: var(--teal); letter-spacing: .4px; }
  .when { letter-spacing: 2.5px; }
  .frame { position: absolute; }
  .details { font-size: 14px; line-height: 17.5px; letter-spacing: 1.8px; }
  .details p + p { margin-top: 6px; }
</style>
</head>
<body>

<!-- Portrait invitation -->
<section class="card card--main" aria-label="Portrait invitation">
  <div class="art art--flipflops" style="left:0;top:0;width:112px;height:155px" role="img" aria-label="Pair of pink flip-flops"></div>
  <div class="art art--hat" style="left:226px;top:0;width:104px;height:48px" role="img" aria-label="Summer hat"></div>
  <div class="art art--melon" style="left:412px;top:15px;width:138px;height:95px" role="img" aria-label="Watermelon slice"></div>
  <div class="art art--camera" style="left:492px;top:168px;width:58px;height:74px" role="img" aria-label="Holiday camera"></div>
  <div class="art art--orange" style="left:-6px;top:272px;width:62px;height:68px" role="img" aria-label="Orange slice"></div>
  <div class="art art--shades" style="left:0;top:412px;width:96px;height:62px" role="img" aria-label="Sunglasses"></div>
  <div class="art art--cocktail" style="left:438px;top:358px;width:108px;height:124px" role="img" aria-label="Cocktail glass with lime"></div>
  <div class="art art--bag" style="left:0;top:596px;width:58px;height:181px" role="img" aria-label="Striped beach bag"></div>
  <div class="art art--ring" style="left:490px;top:640px;width:60px;height:130px" role="img" aria-label="Life ring"></div>
  <div class="art art--star" style="left:250px;top:742px;width:76px;height:35px" role="img" aria-label="Starfish"></div>

  <p class="line intro" style="top:60px">LEAVE THE KIDS AT HOME<br>AND LET YOUR HAIR DOWN AT</p>
  <div class="art art--sun" style="left:175px;top:128px;width:200px;height:60px" role="img" aria-label="Sun with wave ornaments"></div>
  <p class="line hosts" style="top:203px;font-size:34px">Simon &amp; Lorna's</p>
  <div class="rule" style="left:62px;top:252px;width:425px"></div>
  <p class="line title" style="top:262px;font-size:29px">YULETIDE UNWIND BASH</p>
  <div class="rule" style="left:62px;top:304px;width:425px"></div>
  <svg class="ribbon" style="left:100px;top:315px" width="350" height="32" viewBox="0 0 350 32">
    <polygon points="0,1 349,1 333,16 349,31 0,31 16,16" fill="none" stroke="var(--teal)" stroke-width="2"/>
  </svg>
  <p class="line ribbon-text" style="top:322px;font-size:13px">FOR WATTLE BEND AND FRIENDS</p>
  <p class="line when" style="top:368px;font-size:22px;letter-spacing:3px">SATURDAY 2 JANUARY</p>
  <p class="line when" style="top:404px;font-size:18px">FROM 6PM 'TIL LATE</p>
  <p class="line when" style="top:435px;font-size:19px">25 BANKSIA STREET, WATTLE BEND</p>

  <svg class="frame" style="left:66px;top:496px" width="418" height="240" viewBox="0 0 418 240">
    <path d="M10 8 Q110 0 209 8 T408 8 Q400 120 408 232 Q309 240 209 232 T10 232 Q18 120 10 8 Z" fill="none" stroke="var(--teal)" stroke-width="2"/>
    <path d="M16 14 Q112 7 209 14 T402 14 Q395 120 402 226 Q306 233 209 226 T16 226 Q23 120 16 14 Z" fill="none" stroke="var(--teal)" stroke-width="1.2"/>
  </svg>
  <div class="line details" style="top:516px">
    <p>CHILD-FREE EVENT<br>DRESS: SUMMER CASUAL, BARE FEET WELCOME<br>COCKTAIL FOOD PROVIDED<br>BYO BUT ONLY IF YOU INSIST</p>
    <p>IF YOU HAVE SOME FRIENDS OR NEIGHBOURS<br>THAT YOU LIKE TO HANG OUT WITH, WE WOULD<br>LOVE TO MEET, BRING THEM WITH YOU!</p>
    <p>AN RSVP FOR CATERING WOULD BE NICE.<br>TEXT SIMON XXX XXXXXX<br>OR LORNA YYY YYYYYY BEFORE XMAS PLEASE.</p>
  </div>
</section>

<!-- Landscape front -->
<section class="card card--front" aria-label="Landscape invitation front">
  <div class="art art--flipflops" style="left:0;top:0;width:85px;height:100px" role="img" aria-label="Pair of pink flip-flops"></div>
  <div class="art art--hat" style="left:225px;top:0;width:95px;height:28px" role="img" aria-label="Summer hat"></div>
  <div class="art art--melon" style="left:440px;top:0;width:90px;height:60px" role="img" aria-label="Watermelon slice"></div>
  <div class="art art--camera" style="left:486px;top:116px;width:44px;height:52px" role="img" aria-label="Holiday camera"></div>
  <div class="art art--orange" style="left:-6px;top:164px;width:58px;height:64px" role="img" aria-label="Orange slice"></div>
  <div class="art art--shades" style="left:0;top:255px;width:58px;height:36px" role="img" aria-label="Sunglasses"></div>
  <div class="art art--cocktail" style="left:488px;top:244px;width:42px;height:56px" role="img" aria-label="Cocktail glass with lime"></div>
  <div class="art art--ring" style="left:470px;top:336px;width:70px;height:50px" role="img" aria-label="Life ring"></div>
  <div class="art art--bag" style="left:0;top:342px;width:50px;height:28px" role="img" aria-label="Striped beach bag"></div>

  <p class="line intro" style="top:42px;font-size:15px;letter-spacing:1.8px">LEAVE THE KIDS AT HOME AND LET<br>YOUR HAIR DOWN AT</p>
  <div class="art art--sun" style="left:215px;top:90px;width:100px;height:30px" role="img" aria-label="Sun with wave ornaments"></div>
  <p class="line hosts" style="top:122px;font-size:32px">Simon &amp; Lorna's</p>
  <div class="rule" style="left:74px;top:175px;width:406px"></div>
  <p class="line title" style="top:186px;font-size:28px">YULETIDE UNWIND BASH</p>
  <div class="rule" style="left:74px;top:232px;width:406px"></div>
  <svg class="ribbon" style="left:108px;top:245px" width="340" height="32" viewBox="0 0 340 32">
    <polygon points="0,1 339,1 323,16 339,31 0,31 16,16" fill="none" stroke="var(--teal)" stroke-width="2"/>
  </svg>
  <p class="line ribbon-text" style="top:252px;font-size:13.5px">FOR WATTLE BEND AND FRIENDS</p>
  <p class="line when" style="top:289px;font-size:19px;letter-spacing:2.2px">SATURDAY 2 JANUARY</p>
  <p class="line when" style="top:314px;font-size:19px;letter-spacing:2.2px">FROM 6PM 'TIL LATE</p>
  <p class="line when" style="top:339px;font-size:19px;letter-spacing:2.2px">25 BANKSIA STREET, WATTLE BEND</p>
</section>

<!-- Landscape details -->
<section class="card card--details" aria-label="Landscape invitation details">
  <div class="art art--hat" style="left:222px;top:0;width:98px;height:30px" role="img" aria-label="Summer hat"></div>
  <div class="art art--flipflops" style="left:0;top:10px;width:60px;height:75px" role="img" aria-label="Pair of pink flip-flops"></div>
  <div class="art art--melon" style="left:440px;top:0;width:90px;height:60px" role="img" aria-label="Watermelon slice"></div>
  <div class="art art--camera" style="left:490px;top:122px;width:40px;height:56px" role="img" aria-label="Holiday camera"></div>
  <div class="art art--orange" style="left:-6px;top:164px;width:58px;height:64px" role="img" aria-label="Orange slice"></div>
  <div class="art art--shades" style="left:0;top:255px;width:58px;height:35px" role="img" aria-label="Sunglasses"></div>
  <div class="art art--cocktail" style="left:492px;top:226px;width:38px;height:70px" role="img" aria-label="Cocktail glass with lime"></div>
  <div class="art art--ring" style="left:488px;top:340px;width:60px;height:40px" role="img" aria-label="Life ring"></div>

  <div class="art art--sun" style="left:200px;top:46px;width:124px;height:34px" role="img" aria-label="Sun with wave ornaments"></div>
  <svg class="frame" style="left:63px;top:84px" width="422" height="260" viewBox="0 0 422 260">
    <path d="M10 8 Q110 0 211 8 T412 8 Q404 130 412 252 Q311 260 211 252 T10 252 Q18 130 10 8 Z" fill="none" stroke="var(--teal)" stroke-width="2"/>
    <path d="M16 14 Q112 7 211 14 T406 14 Q399 130 406 246 Q308 253 211 246 T16 246 Q23 130 16 14 Z" fill="none" stroke="var(--teal)" stroke-width="1.2"/>
  </svg>
  <div class="line details" style="top:109px;font-size:14px;line-height:19.3px;letter-spacing:1.7px">
    <p>CHILD-FREE EVENT<br>DRESS: SUMMER CASUAL, BARE FEET WELCOME<br>COCKTAIL FOOD PROVIDED<br>BYO BUT ONLY IF YOU INSIST</p>
    <p>IF YOU HAVE SOME FRIENDS OR NEIGHBOURS<br>THAT YOU LIKE TO HANG OUT WITH, WE WOULD<br>LOVE TO MEET, BRING THEM WITH YOU!</p>
    <p>AN RSVP FOR CATERING WOULD BE NICE.<br>TEXT SIMON XXX XXXXXX<br>OR LORNA YYY YYYYYY BEFORE XMAS PLEASE.</p>
  </div>
</section>

</body>
</html>
```